Belvanta - Awnings & Outdoor Blinds

We need a brochure design for out Australia based Awnings & Outdoor Blinds company.

We require 2 templates:

1. Product Specific. (For One Product) - Single or Double Sided A4
Must Include:
Our Logo, Product Description, Pictures,Product Features & Benefits (in point form) & Our Contact Details (Phone & Website).

2.Product Range (Our Full Range) - 8 Page A4 (2x A3 Folded In Half Printed Both Sides).
Must Include:
Page 1 - Front Cover - Title (Product Range) Cover With Our Logo & Photo/s.
Page 2 - About Us, Why Us & Warranty Information.
Page 3 - A Gallery (Just Photos Showcasing Our Work)
Page 4 - 3 Products Per Page (Image/s, Product Title & Brief Description).
Page 5 - 3 Products Per Page (Image/s, Product Title & Brief Description).
Page 6 - 3 Products Per Page (Image/s, Product Title & Brief Description).
Page 7 - 3 Products Per Page (Image/s, Product Title & Brief Description).
Page 8 - Back Cover with our Contact Details (Phone, Website & Logo).

We are just looking for templates we will fill in all the content, needs to be easy to customise (change photos/text etc).

For more info on what we do: http://site7305.example-builder.com/belvanta

Requirements
Nice to have
• Nice to have the product pages 4 - 7 not as identical layout.

Nice to be in our colours Red, White, Black, Light Grey. (See Logo Variations - Logo is the top one).

```html
<!DOCTYPE html>
<html lang="en">
<head>
<meta charset="utf-8">
<title>Belvanta – Heavy Duty Channel Flyers</title>
<link rel="stylesheet" href="https://fonts.googleapis.com/css2?family=Arimo:wght@400;700&display=swap">
<style>
  :root {
    --red: #c4161c;
    --red-text: #d2232a;
    --black: #0d0d0d;
    --white: #ffffff;
    --light-grey: #f1f1f1;
    --mid-grey: #8a8a8a;
    --ink: #1c1c1c;
    --stage: #e9e9e9;
    --photo-deck: #6b3a22;
    --photo-lawn: #5f8a45;
    --photo-roof: #4a3a2e;
  }
  * { box-sizing: border-box; margin: 0; padding: 0; }
  html, body { width: 1200px; height: 1000px; overflow: hidden; }
  body {
    background: linear-gradient(180deg, #f4f4f4 0%, var(--stage) 100%);
    font-family: "Arimo", Arial, sans-serif;
    display: flex;
    justify-content: center;
    align-items: center;
    gap: 80px;
  }
  .flyer {
    width: 500px;
    height: 707px;
    background: var(--light-grey);
    color: var(--ink);
    padding-top: 20px;
    display: flex;
    flex-direction: column;
    box-shadow: 0 6px 18px rgba(0,0,0,.18);
  }
  .flyer--dark { background: var(--black); color: var(--white); }

  .flyer__header {
    height: 52px;
    background: var(--red);
    display: flex;
    align-items: center;
    justify-content: space-between;
    padding: 0 26px;
  }
  .flyer--dark .flyer__header { background: var(--white); }
  .flyer__title { font-size: 21px; font-weight: 700; color: var(--white); }
  .flyer--dark .flyer__title { color: var(--red-text); }

  .brand { display: flex; align-items: center; gap: 7px; background: var(--white); padding: 6px 8px; margin-right: -8px; }
  .brand__dot { width: 16px; height: 16px; border-radius: 50%; background: var(--red); }
  .brand__text { display: flex; flex-direction: column; line-height: 1; }
  .brand__name { font-size: 22px; font-weight: 700; color: var(--ink); }
  .brand__tag { font-size: 6.5px; color: var(--mid-grey); margin-top: 2px; letter-spacing: .3px; }

  .flyer__intro { font-size: 10.2px; line-height: 1.4; padding: 14px 26px 0; }

  .gallery {
    margin: 14px 24px 0;
    display: grid;
    grid-template-columns: repeat(4, 1fr);
    gap: 5px;
  }
  .photo {
    border: 3px solid var(--black);
    background: linear-gradient(180deg, var(--photo-roof) 0%, #8e9a8c 22%, var(--photo-lawn) 55%, var(--photo-deck) 78%, #3d2518 100%);
  }
  .flyer--dark .photo { border-color: var(--white); }
  .photo--large { grid-column: span 2; height: 172px; }
  .photo--small { height: 82px; }

  .details {
    display: grid;
    grid-template-columns: 1fr 1fr;
    gap: 22px;
    padding: 20px 26px 0;
    flex: 1;
  }
  .details__heading { color: var(--red-text); font-size: 12px; margin-bottom: 7px; }
  .details__text { font-size: 9.6px; line-height: 1.4; margin-bottom: 14px; }
  .benefits { list-style: none; }
  .benefits li {
    font-size: 10.2px; line-height: 1.35; text-align: justify;
    padding-left: 10px; position: relative; margin-bottom: 14px;
  }
  .benefits li::before {
    content: ""; position: absolute; left: 0; top: 4px;
    width: 5px; height: 5px; background: var(--red);
  }

  .flyer__footer {
    text-align: center; color: var(--red-text);
    font-size: 8.6px; line-height: 1.55; padding: 0 20px 22px;
  }
</style>
</head>
<body>

<article class="flyer flyer--light">
  <header class="flyer__header">
    <h1 class="flyer__title">Heavy Duty Channel</h1>
    <div class="brand"><span class="brand__dot"></span><span class="brand__text"><span class="brand__name">Belvanta</span><span class="brand__tag">Awnings &amp; Outdoor Blinds</span></span></div>
  </header>
  <p class="flyer__intro">The Heavy Duty Channel System is perfect for larger sized applications capable of reaching spans of upto 5.8m in width, includes a powder coated aluminum guide system to smoothly guide the vertical path of the blind as well as locking pins for adjustable lock-down levels.</p>
  <div class="gallery">
    <div class="photo photo--large" role="img" aria-label="Outdoor patio enclosed by channel blinds with dining set and pool view"></div>
    <div class="photo photo--large" role="img" aria-label="Outdoor patio enclosed by channel blinds with dining set and pool view"></div>
    <div class="photo photo--small" role="img" aria-label="Patio blind installation thumbnail"></div>
    <div class="photo photo--small" role="img" aria-label="Patio blind installation thumbnail"></div>
    <div class="photo photo--small" role="img" aria-label="Patio blind installation thumbnail"></div>
    <div class="photo photo--small" role="img" aria-label="Patio blind installation thumbnail"></div>
  </div>
  <section class="details">
    <div>
      <h2 class="details__heading">Features &amp; Benefits:</h2>
      <ul class="benefits">
        <li>Durable fabrics: Many of the fabrics we use are manufactured in Australia to suit local conditions. Choose from sunscreen, acrylic or canvas fabrics knowing they will look great for many years.</li>
        <li>Technically superior materials: We make our Drop-Arm Fabric Awnings from components that have been engineered to last in Australia’s harsh conditions.</li>
        <li>Technically superior materials: We make our Drop-Arm Fabric Awnings from components that have been engineered to last in Australia’s harsh conditions</li>
      </ul>
    </div>
    <div>
      <h2 class="details__heading">Operation:</h2>
      <p class="details__text">Crank Operation (Gearbox) as standard, Can also be rmotorised with optional Sun &amp; Wind Sensors.</p>
      <h2 class="details__heading">Available Fabrics:</h2>
      <p class="details__text">Available in our Sunscreen &amp; Block Out abrics.</p>
      <h2 class="details__heading">Specifications:</h2>
      <p class="details__text">Maximum Width: 5800mm,<br>Maximum Drop: 3200mm,<br>Side Channel Width: 50mm.</p>
    </div>
  </section>
  <footer class="flyer__footer">Belvanta - Outdoor Blinds &nbsp;| Unit 8 - 12 Harbour Rd, Wynnum, | &nbsp;Brisbane QLD 4178.<br>Phone: 1300 482 716 &nbsp;| &nbsp;Email: info@belvanta.com.au &nbsp;| &nbsp;www.belvanta.com</footer>
</article>

<article class="flyer flyer--dark">
  <header class="flyer__header">
    <h1 class="flyer__title">Heavy Duty Channel</h1>
    <div class="brand"><span class="brand__dot"></span><span class="brand__text"><span class="brand__name">Belvanta</span><span class="brand__tag">Awnings &amp; Outdoor Blinds</span></span></div>
  </header>
  <p class="flyer__intro">The Heavy Duty Channel System is perfect for larger sized applications capable of reaching spans of upto 5.8m in width, includes a powder coated aluminum guide system to smoothly guide the vertical path of the blind as well as locking pins for adjustable lock-down levels.</p>
  <div class="gallery">
    <div class="photo photo--large" role="img" aria-label="Outdoor patio enclosed by channel blinds with dining set and pool view"></div>
    <div class="photo photo--large" role="img" aria-label="Outdoor patio enclosed by channel blinds with dining set and pool view"></div>
    <div class="photo photo--small" role="img" aria-label="Patio blind installation thumbnail"></div>
    <div class="photo photo--small" role="img" aria-label="Patio blind installation thumbnail"></div>
    <div class="photo photo--small" role="img" aria-label="Patio blind installation thumbnail"></div>
    <div class="photo photo--small" role="img" aria-label="Patio blind installation thumbnail"></div>
  </div>
  <section class="details">
    <div>
      <h2 class="details__heading">Features &amp; Benefits:</h2>
      <ul class="benefits">
        <li>Durable fabrics: Many of the fabrics we use are manufactured in Australia to suit local conditions. Choose from sunscreen, acrylic or canvas fabrics knowing they will look great for many years.</li>
        <li>Technically superior materials: We make our Drop-Arm Fabric Awnings from components that have been engineered to last in Australia’s harsh conditions.</li>
        <li>Technically superior materials: We make our Drop-Arm Fabric Awnings from components that have been engineered to last in Australia’s harsh conditions.</li>
      </ul>
    </div>
    <div>
      <h2 class="details__heading">Operation:</h2>
      <p class="details__text">Crank Operation (Gearbox) as standard, Can also be rmotorised with optional Sun &amp; Wind Sensors.</p>
      <h2 class="details__heading">Available Fabrics:</h2>
      <p class="details__text">Available in our Sunscreen &amp; Block Out abrics.</p>
      <h2 class="details__heading">Specifications:</h2>
      <p class="details__text">Maximum Width: 5800mm,<br>Maximum Drop: 3200mm,<br>Side Channel Width: 50mm.</p>
    </div>
  </section>
  <footer class="flyer__footer">Belvanta - Outdoor Blinds &nbsp;| Unit 8 - 12 Harbour Rd, Wynnum, | &nbsp;Brisbane QLD 4178.<br>Phone: 1300 482 716 &nbsp;| &nbsp;Email: info@belvanta.com.au &nbsp;| &nbsp;www.belvanta.com</footer>
</article>

</body>
</html>
```